Live a healthy life. Kvel

Advertising campaign for reversing type 2 diabetes and insulin resistance. The best way to reverse type 2 diabetes or put it in remission is to prevent it from triggering. We do this by healthy food choices, no overeating and exercise. The final design should promote the aforementioned and should be able to be implemented in society, schools, churches etc. Kvel is the creator of the campaign. Youtube channel "out of the head of Kvel"

```html
<!DOCTYPE html>
<html lang="en">
<head>
<meta charset="utf-8">
<title>Reverse Type 2 Diabetes – Kvel</title>
<link rel="stylesheet" href="https://fonts.googleapis.com/css2?family=Fira+Sans:ital,wght@0,400;0,500;0,600;0,700;0,800;1,600&display=swap">
<style>
  :root {
    --cream: #fbf0df;
    --teal: #0e7a80;
    --teal-text: #137d83;
    --yellow: #f6c55f;
    --orange: #e87c1e;
    --peach: #f7dfc0;
    --sage: #b6d0c4;
    --ink: #1e2b30;
    --white: #fdf6ea;
    --mint: #0bc4b8;
    --coral: #f36f5b;
    --red: #d83b2e;
  }
  * { margin: 0; padding: 0; box-sizing: border-box; }
  html, body { width: 800px; height: 1200px; overflow: hidden; background: var(--cream); }
  body { font-family: "Fira Sans", sans-serif; }
  .poster { position: relative; width: 800px; height: 1200px; overflow: hidden; background: var(--cream); }
  .backdrop { position: absolute; inset: 0; }

  .title-panel {
    position: absolute; left: 30px; top: 30px; width: 741px; height: 185px;
    background: var(--teal); border-radius: 12px; text-align: center;
  }
  .title-main {
    position: absolute; left: 0; right: 0; top: 5px;
    color: var(--yellow); font-weight: 700; font-size: 114px; line-height: 1; letter-spacing: 5px;
  }
  .title-sub {
    position: absolute; left: 0; right: 0; top: 107px;
    color: var(--white); font-weight: 700; font-size: 71px; line-height: 1; letter-spacing: 4px;
  }

  .hero-art {
    position: absolute; left: 30px; top: 252px; width: 370px; height: 288px;
    background: linear-gradient(90deg, var(--coral) 0 45%, var(--mint) 45% 100%);
    border-radius: 150px 150px 0 0; opacity: .9;
  }

  .prevention { position: absolute; left: 427px; top: 232px; width: 360px; }
  .prevention-heading {
    color: var(--orange); font-weight: 700; font-size: 44px; line-height: 51px; letter-spacing: 1px;
  }
  .prevention-text {
    margin-top: 12px; color: var(--ink); font-weight: 500; font-size: 27px; line-height: 32px;
  }
  .prevention-text em { color: var(--orange); font-style: italic; font-weight: 600; }

  .steps-banner {
    position: absolute; left: 30px; top: 541px; width: 741px; height: 92px;
    background: var(--teal); border-radius: 12px;
    color: var(--white); font-weight: 600; font-size: 45px; line-height: 92px; text-align: center;
  }

  .step-icon {
    position: absolute; width: 148px; height: 148px; border-radius: 50%;
    background: var(--yellow); border: 7px solid var(--teal);
  }
  .step-icon .icon-art {
    position: absolute; left: 24px; top: 24px; width: 86px; height: 86px; border-radius: 50%;
    background: #8fc9c2; opacity: .75;
  }
  .step-icon--food { left: 67px; top: 641px; }
  .step-icon--plate { left: 162px; top: 796px; }
  .step-icon--move { left: 67px; top: 952px; }

  .step { position: absolute; }
  .step-title { color: var(--orange); font-weight: 600; font-size: 45px; line-height: 1; }
  .step-text { margin-top: 10px; font-size: 21px; line-height: 25px; font-weight: 500; }
  .step--food { left: 239px; top: 652px; }
  .step--food .step-text { color: var(--teal-text); }
  .step--plate { left: 333px; top: 808px; }
  .step--plate .step-text { color: var(--ink); }
  .step--move { left: 239px; top: 963px; }
  .step--move .step-text { color: var(--ink); }

  .creator-mark {
    position: absolute; left: 356px; top: 1110px; width: 90px; text-align: center;
    color: var(--orange); font-weight: 800; font-size: 30px; line-height: 50px;
  }

  .channel-pill {
    position: absolute; left: 467px; top: 1096px; width: 360px; height: 74px;
    background: var(--yellow); border-radius: 37px 0 0 37px;
    display: flex; align-items: center; padding-left: 28px; gap: 14px;
  }
  .channel-dot { width: 30px; height: 30px; border-radius: 50%; background: var(--red); flex: none; }
  .channel-name { color: var(--ink); font-weight: 500; font-size: 21px; white-space: nowrap; }
</style>
</head>
<body>
<main class="poster">
  <svg class="backdrop" width="800" height="1200" viewBox="0 0 800 1200" aria-hidden="true">
    <path d="M0 0 H90 C150 60 120 180 180 230 C260 300 380 260 390 380 C398 480 320 540 260 540 H0 Z" fill="var(--orange)"/>
    <path d="M0 0 H80 C140 60 110 175 170 222 C250 290 370 255 378 375 C384 470 310 528 250 528 H0 Z" fill="var(--yellow)"/>
    <path d="M800 530 C720 540 600 560 560 600 C450 700 520 820 640 900 C720 950 760 1060 800 1100 Z" fill="var(--peach)"/>
    <path d="M0 820 C60 900 30 1020 140 1100 C220 1160 290 1180 310 1200 H0 Z" fill="var(--sage)"/>
  </svg>

  <header class="title-panel">
    <h1 class="title-main">REVERSE</h1>
    <p class="title-sub">TYPE 2 DIABETES</p>
  </header>

  <div class="hero-art" role="img" aria-label="Illustration of two confident women, one with arms crossed and one flexing her arm"></div>

  <section class="prevention">
    <h2 class="prevention-heading">START WITH<br>PREVENTION.</h2>
    <p class="prevention-text">The best way to reverse or<br>stop type 2 diabetes is to<br><em>prevent it from starting.</em><br>Let’s make healthy living<br>a lifestyle!</p>
  </section>

  <h2 class="steps-banner">3 Simple Steps to Fight Diabetes</h2>

  <div class="step-icon step-icon--food"><div class="icon-art" role="img" aria-label="Salad bowl icon"></div></div>
  <section class="step step--food">
    <h3 class="step-title">Eat Smart</h3>
    <p class="step-text">Choose real healthy food:<br>Fruits, veggies, lean proteins and whole grains.<br>Avoid sugary snacks, soda and fried foods</p>
  </section>

  <div class="step-icon step-icon--plate"><div class="icon-art" role="img" aria-label="Plate with fork and knife icon"></div></div>
  <section class="step step--plate">
    <h3 class="step-title">Don’t Overeat</h3>
    <p class="step-text">Stop when you are full.<br>Choose portion control over plate overload.</p>
  </section>

  <div class="step-icon step-icon--move"><div class="icon-art" role="img" aria-label="Running person icon"></div></div>
  <section class="step step--move">
    <h3 class="step-title">Move Daily</h3>
    <p class="step-text">Walking, running, riding a bike, dancing, etc.<br>30 minutes a day keeps diabetes away!</p>
  </section>

  <div class="creator-mark">Kvel</div>

  <div class="channel-pill">
    <span class="channel-dot"></span>
    <span class="channel-name">out of the head of Kvel</span>
  </div>
</main>
</body>
</html>
```